Tessaline Bioscience Advisors.

Molecular Technology Consulting. Feasibility, Evaluation and Validation of ISH/IHC and Imaging Applications.

Industry/Entity Type

Consulting

Contact Information for Business Card

Tessaline Bioscience Advisors
Cell: 330 555-0147
Dorian Makepeace
dmakepeace7804@quillmail.test

```html
<!DOCTYPE html>
<html lang="en">
<head>
<meta charset="utf-8">
<title>Tessaline Bioscience Advisors — Business Card</title>
<link rel="stylesheet" href="https://fonts.googleapis.com/css2?family=Cinzel:wght@700&family=Lato:wght@400;700&display=swap">
<style>
  :root {
    --navy: #27286e;
    --orange: #f47b20;
    --card: #ffffff;
    --backdrop: #e4e4e6;
    --card-shadow: rgba(0, 0, 0, 0.18);
  }
  * { box-sizing: border-box; margin: 0; padding: 0; }
  html, body {
    width: 1200px;
    height: 1000px;
    overflow: hidden;
    background: var(--backdrop);
  }
  .canvas {
    position: relative;
    width: 1200px;
    height: 1000px;
  }
  .card {
    position: absolute;
    left: 250px;
    width: 700px;
    height: 400px;
    background: var(--card);
    box-shadow: 0 6px 18px var(--card-shadow);
    overflow: hidden;
  }
  .card--brand { top: 60px; }
  .card--contact { top: 540px; }

  .brand-mark {
    position: absolute;
    left: -90px;
    top: 50px;
    width: 300px;
    height: 300px;
    border-radius: 50%;
    background: var(--orange);
  }
  .brand-name {
    position: absolute;
    left: 260px;
    top: 140px;
    font-family: "Cinzel", serif;
    font-weight: 700;
    color: var(--navy);
    font-size: 34px;
    line-height: 1.2;
    letter-spacing: 0.5px;
  }

  .contact-lockup {
    position: absolute;
    left: 60px;
    top: 60px;
    display: flex;
    align-items: center;
    gap: 18px;
  }
  .contact-lockup .dot {
    width: 34px;
    height: 34px;
    border-radius: 50%;
    background: var(--orange);
    flex: none;
  }
  .contact-lockup .company {
    font-family: "Cinzel", serif;
    font-weight: 700;
    color: var(--navy);
    font-size: 26px;
    line-height: 1.2;
  }
  .person {
    position: absolute;
    left: 60px;
    top: 205px;
    font-family: "Cinzel", serif;
    font-weight: 700;
    color: var(--navy);
    font-size: 26px;
    letter-spacing: 0.5px;
  }
  .details {
    position: absolute;
    left: 60px;
    top: 262px;
    list-style: none;
    font-family: "Lato", sans-serif;
    font-size: 22px;
    line-height: 1.75;
  }
  .details .label { color: var(--navy); font-weight: 700; margin-right: 6px; }
  .details .value { color: var(--orange); letter-spacing: 0.5px; }
</style>
</head>
<body>
<main class="canvas">
  <section class="card card--brand" aria-label="Card front">
    <div class="brand-mark"></div>
    <h1 class="brand-name">Tessaline Bioscience<br>Advisors</h1>
  </section>

  <section class="card card--contact" aria-label="Card back">
    <div class="contact-lockup">
      <span class="dot"></span>
      <p class="company">TESSALINE BIOSCIENCE<br>ADVISORS</p>
    </div>
    <h2 class="person">DORIAN MAKEPEACE</h2>
    <ul class="details">
      <li><span class="label">M:</span><span class="value">330 555-0147</span></li>
      <li><span class="label">E:</span><span class="value">dmakepeace7804@quillmail.test</span></li>
    </ul>
  </section>
</main>
</body>
</html>
```